Halvor Interiors Studio New Business Card

I am opening a new division of my business. I am a high end interior designer, and the new business is writing specs for construction projects. It will be marketed to the VERY high end contractor, architects and realtors. The client will actually be the one who pays us and signs the agreement, but it will be the contractor, architect or realtor that will recommend us. I have attached my current card and our previous logo which is still used on some of our paperwork. I would like the new logo to be connected in some way to what we are currently using. We will need to have room on the card for a person's name. I'd like to omit the address as we might be moving the office soon. The web address is www.HalvorInteriorsStudio.example. For this design, please use my name, Marisol Fenwick.

Target Market(s)

High End Luxury Contractors, Realtors and Architects

Industry/Entity Type

Residential Construction

Contact Information for Business Card

Halvor Interiors Studio, Phone: 555-204-9167, www.HalvorInteriorsStudio.example , Marisol Fenwick

Font styles to use
Sans Serif

Colors
ec1f27

Requirements
Must have
• Some visual reference to my current card and logos. Use the colors submitted on the business card I attached.
Nice to have
• A visual reference to my current card and logos. Use the colors submitted on the card I attached.
Should not have
• A physical address

```html
<!DOCTYPE html>
<html lang="en">
<head>
<meta charset="utf-8">
<title>Marisol Fenwick – Business Card</title>
<link href="https://fonts.googleapis.com/css2?family=Marcellus&family=Open+Sans:wght@400;600&display=swap" rel="stylesheet">
<style>
  :root {
    --rust: #8a331d;
    --paper: #ffffff;
    --ink-grey: #7a7a7a;
    --rule-grey: #9a9a9a;
    --backdrop: #e9e6e2;
  }
  * { margin: 0; padding: 0; box-sizing: border-box; }
  html, body { width: 1200px; height: 1000px; overflow: hidden; }
  body { background: var(--backdrop); position: relative; font-family: "Open Sans", sans-serif; }

  .card { position: absolute; left: 265px; width: 665px; height: 397px; }
  .card--front { top: 73px; background: var(--paper); }
  .card--back { top: 532px; background: var(--rust); }

  .brand { position: absolute; text-align: center; }
  .brand__mark { display: block; margin: 0 auto; }
  .brand__name {
    font-family: "Marcellus", sans-serif; font-weight: 400; letter-spacing: 0.04em;
    white-space: nowrap; line-height: 1;
  }
  .brand__rule { height: 1px; margin-top: 6px; }
  .brand__tagline {
    font-family: "Marcellus", sans-serif; letter-spacing: 0.22em; white-space: nowrap; margin-top: 5px;
  }

  .card--front .brand { left: 40px; top: 139px; width: 275px; }
  .card--front .brand__mark { width: 55px; height: 55px; background: var(--rust); margin-bottom: 18px; }
  .card--front .brand__name { color: var(--ink-grey); font-size: 26px; }
  .card--front .brand__rule { background: var(--rule-grey); }
  .card--front .brand__tagline { color: var(--ink-grey); font-size: 10px; }

  .contact { position: absolute; left: 350px; top: 133px; width: 290px; }
  .contact__name { color: var(--rust); font-weight: 600; font-size: 18px; letter-spacing: 0.01em; margin-bottom: 36px; }
  .contact__list { list-style: none; }
  .contact__item {
    display: flex; align-items: center; gap: 8px; color: var(--ink-grey);
    font-size: 14px; line-height: 24px; white-space: nowrap;
  }
  .contact__icon { width: 13px; height: 13px; fill: var(--rust); flex: none; }

  .card--back .brand { left: 130px; top: 115px; width: 405px; }
  .card--back .brand__mark { width: 78px; height: 78px; background: var(--paper); margin-bottom: 22px; }
  .card--back .brand__name { color: var(--paper); font-size: 36px; }
  .card--back .brand__rule { background: rgba(255,255,255,0.7); }
  .card--back .brand__tagline { color: var(--paper); font-size: 13px; }
</style>
</head>
<body>
  <section class="card card--front">
    <div class="brand">
      <span class="brand__mark"></span>
      <div class="brand__name">MARISOL FENWICK</div>
      <div class="brand__rule"></div>
      <div class="brand__tagline">COMMERCIAL | RESIDENTIAL DESIGN</div>
    </div>
    <div class="contact">
      <div class="contact__name">MARISOL FENWICK</div>
      <ul class="contact__list">
        <li class="contact__item">
          <svg class="contact__icon" viewBox="0 0 14 14"><path d="M1 5c0-2 3-3 6-3s6 1 6 3v1h-3V5H4v1H1z"/><path d="M3 7h8l1 5H2z"/></svg>
          555.204.9167
        </li>
        <li class="contact__item">
          <svg class="contact__icon" viewBox="0 0 14 14"><path d="M1 3h12v1L7 8 1 4z"/><path d="M1 5.5l6 4 6-4V11H1z"/></svg>
          marisol@halvorinteriorsstudio.example
        </li>
        <li class="contact__item">
          <svg class="contact__icon" viewBox="0 0 14 14"><path d="M1 2h12v8H1zM2.5 3.5v5h9v-5z"/><path d="M5 11h4v1.5H5z"/></svg>
          www.halvorinteriorsstudio.example
        </li>
      </ul>
    </div>
  </section>

  <section class="card card--back">
    <div class="brand">
      <span class="brand__mark"></span>
      <div class="brand__name">MARISOL FENWICK</div>
      <div class="brand__rule"></div>
      <div class="brand__tagline">COMMERCIAL | RESIDENTIAL DESIGN</div>
    </div>
  </section>
</body>
</html>
```